Effectively Manage Muscular Pain /with Remedial Massage

A flyer to sell remedial massage Therapy for muscular pain .

$10 Discount with this flyer

Use colors orange and Blak with the color of the logo provided and preferably the fonts as well .

Little spin about remedial massage:

Remedial massage is a deep massage , to create the conditions for the body’s return to normal health after injury or with muscular-skeletal disorders. It is used to treat chronic muscular-skeletal imbalances, strains, sprains, broken bones, bruising or any injury. Deep tissue massage removes blockages, damaged cells, scar tissue and adhesions [speeds up recovery Remedial massage is also used for conditions created by lifestyle for example Repetitive strain injury and Back pain.

Target Market(s)

young professionals with kids , modern suburban couples

Industry/Entity Type

Massage

Requirements
Must have
• doble sided.

Address 418 kelvinhurst Rd , Westbrook Book Now 94620387

```html
<!DOCTYPE html>
<html lang="en">
<head>
<meta charset="utf-8">
<title>Remedial Massage Flyer – Front and Back</title>
<link href="https://fonts.googleapis.com/css2?family=Arimo:wght@400;700&family=Oswald:wght@300;400&display=swap" rel="stylesheet">
<style>
  :root {
    --orange: #f26522;
    --ink: #231f20;
    --white: #ffffff;
    --stage: #1b1f21;
    --photo-light: #f4f4f4;
    --photo-mid: #c9c9c9;
    --photo-blue: #b9cbe6;
  }
  * { margin: 0; padding: 0; box-sizing: border-box; }
  html, body {
    width: 1200px; height: 1172px; overflow: hidden;
    background: var(--stage);
  }
  .canvas { position: relative; width: 1200px; height: 1172px; }

  .flyer {
    position: absolute;
    width: 518px; height: 880px;
    overflow: hidden; background: var(--white);
    font-family: "Arimo", Arial, sans-serif;
  }
  .flyer--front { left: 67px; top: 119px; }
  .flyer--back { left: 614px; top: 150px; }

  .flyer__shapes { position: absolute; inset: 0; width: 518px; height: 880px; }

  .photo { position: absolute; left: 0; top: 0; width: 518px; }
  .photo--back-pain {
    height: 480px;
    background: radial-gradient(ellipse at 45% 55%, #e9a3a3 0%, var(--photo-mid) 30%, var(--photo-light) 70%);
  }
  .photo--neck-pain {
    height: 470px;
    background: linear-gradient(200deg, var(--white) 35%, #e9e4df 60%, var(--photo-blue) 100%);
  }

  .brand { position: absolute; text-align: center; }
  .brand__mark {
    display: block; margin: 0 auto;
    width: 80px; height: 80px; border-radius: 50%;
    background: var(--orange);
  }
  .brand__name {
    display: block; margin-top: 8px;
    font-family: "Oswald", "Arial Narrow", sans-serif;
    font-weight: 400; font-size: 26px; line-height: 30px; letter-spacing: 3px;
  }
  .flyer--front .brand { left: 88px; top: 468px; width: 80px; }
  .flyer--front .brand__name { color: var(--white); }
  .flyer--back .brand { left: 364px; top: 36px; width: 80px; }
  .flyer--back .brand__name { color: var(--ink); }

  .services {
    position: absolute; left: 242px; top: 486px;
    font-family: "Oswald", "Arial Narrow", sans-serif;
    font-weight: 300; font-size: 35px; line-height: 41px;
    color: var(--white); text-transform: uppercase;
  }

  .headline, .offer, .contact-line {
    position: absolute; left: 0; width: 518px; text-align: center;
    font-weight: 700; text-transform: uppercase;
  }
  .headline { top: 612px; font-size: 26px; line-height: 33px; color: var(--white); }
  .offer { top: 702px; font-size: 26px; line-height: 33px; color: var(--orange); }
  .flyer--front .contact-line { top: 802px; font-size: 26px; line-height: 34px; color: var(--white); }

  .book-now {
    position: absolute; left: 304px; top: 182px; width: 200px;
    text-align: center; font-weight: 700; font-size: 26px; line-height: 33px;
    color: var(--ink);
  }

  .about {
    position: absolute; left: 31px; top: 492px; width: 442px;
    font-size: 16.6px; line-height: 21.9px; color: var(--white);
  }
  .about p + p { margin-top: 21.9px; }

  .contact-title {
    position: absolute; left: 0; top: 797px; width: 518px;
    text-align: center; font-weight: 700; font-size: 17px; color: var(--white);
  }
  .flyer--back .contact-line { top: 829px; font-size: 16px; line-height: 22px; color: var(--white); }
</style>
</head>
<body>
<main class="canvas">

  <section class="flyer flyer--front" aria-label="Flyer front">
    <div class="photo photo--back-pain" role="img" aria-label="Photo of a hand pressed on a sore lower back, pain area glowing red"></div>
    <svg class="flyer__shapes" viewBox="0 0 518 880" aria-hidden="true">
      <path d="M0 472 C140 400 330 395 518 424 L518 880 L0 880 Z" fill="var(--ink)"/>
      <path d="M0 781 C180 784 360 772 518 752 L518 880 L0 880 Z" fill="var(--orange)"/>
    </svg>
    <div class="brand">
      <span class="brand__mark"></span>
      <span class="brand__name">KOVA</span>
    </div>
    <p class="services">Osteopathy<br>Clinical Pilates</p>
    <h1 class="headline">Remedial Massage Therapy<br>for Muscular Pain</h1>
    <p class="offer">$10 Discount with<br>this flyer</p>
    <p class="contact-line">Address 418 Kelvinhurst Rd ,<br>Westbrook Book Now 94620387</p>
  </section>

  <section class="flyer flyer--back" aria-label="Flyer back">
    <div class="photo photo--neck-pain" role="img" aria-label="Photo of a woman in a blue shirt holding her sore neck"></div>
    <svg class="flyer__shapes" viewBox="0 0 518 880" aria-hidden="true">
      <path d="M0 446 C150 444 350 440 518 432 L518 880 L0 880 Z" fill="var(--orange)"/>
      <path d="M0 458 C170 450 360 478 518 474 L518 880 L0 880 Z" fill="var(--ink)"/>
      <path d="M0 772 C180 770 360 758 518 738 L518 880 L0 880 Z" fill="var(--orange)"/>
    </svg>
    <div class="brand">
      <span class="brand__mark"></span>
      <span class="brand__name">KOVA</span>
    </div>
    <p class="book-now">BOOK NOW<br>94620387</p>
    <div class="about">
      <p>Remedial massage is a deep massage , to create the conditions for the body’s return to normal health after injury or with muscular-skeletal disorders. It is used to treat chronic muscular-skeletal imbalances, strains, sprains, broken bones, bruising or any injury.</p>
      <p>Deep tissue massage removes blockages, damaged cells, scar tissue and adhesions [speeds up recovery Remedial massage is also used for conditions created by lifestyle for example Repetitive strain injury and Back pain.</p>
    </div>
    <p class="contact-title">CONTACT US</p>
    <p class="contact-line">Address 418 Kelvinhurst Rd ,<br>Westbrook Book Now 94620387</p>
  </section>

</main>
</body>
</html>
```